Powerpoint Design for business and consulting company - Brennig-Tautz

I am searching a design specialist who can help me to create a PowerPoint Design for my company. I'm in the business coaching and consulting industry.

The PPT master should be easy to use and include professional formatting (using the fonts of my website). In general, the slide master should have the look and feel of my website (in terms of fonts, colors, logos, possibility to place big photographs, having text and graph slides as well as photo slides with just 1 key message).

The PowerPoint design should fit my cooperate Identity (please see my website https://brennig-tautz.de).
My logos are attached.

Additional information:
- wide screen format - 16: 9
- right set up of a fitting color scheme
https: // tintrow. io / f6ded1-bfcbce-807f84-9cd3d1-666666
# 666666 (Dim Gray) - body / heading text
# 807F84 (Gray Web)
#BFCBCE (Silver Sand) - link hover
# 9cd3d1 (Powder Blue) - Link color
# F6DED1 (Champagne Pink)

- creation of chart templates, using chart tools, and different chart types etc.
- creation of different slide layouts to place content, pictures (in different sizes), optionally Media
- set up of display guide lines
- as well as standard elements, such as text boxes, lines, default shapes, etc.

• Powerpoint Design needs to have:
https://tintrow.io/f6ded1-bfcbce-807f84-9cd3d1-666666
# 807F84 (Gray Web)
# F6DED1 (Champagne Pink)

```html
<!DOCTYPE html>
<html lang="de">
<head>
<meta charset="utf-8">
<title>Brennig-Tautz – Präsentationsvorlage</title>
<link rel="stylesheet" href="https://fonts.googleapis.com/css2?family=Raleway:wght@300;400;600;700&family=Roboto:wght@400;500;700&family=Open+Sans:wght@400;600&family=Oswald:wght@500&display=swap">
<style>
:root{
  --pink:#f6ded1;
  --sand:#bfcbce;
  --gray:#807f84;
  --teal:#9cd3d1;
  --dim:#666666;
  --paper:#ffffff;
  --canvas:#e3e5e6;
  --soft:#f3f4f4;
  --body:#9a9a9a;
}
*{margin:0;padding:0;box-sizing:border-box}
html,body{width:1200px;height:2360px;overflow:hidden}
body{position:relative;background:var(--canvas);font-family:'Open Sans',sans-serif;color:var(--dim)}
.hero-bg{position:absolute;left:0;top:0;width:1200px;height:545px;background:linear-gradient(100deg,#7d8c90 0%,#a9b4b6 35%,#d5dadb 60%,#e3e5e6 100%)}
.hero-light{position:absolute;left:0;top:0}
.hero-rule{position:absolute;left:462px;top:534px;width:252px;height:1px;background:#9aa6c8}
.title-slide{position:absolute;left:354px;top:69px;width:468px;height:261px;background:var(--paper);overflow:hidden}
.title-slide .band{height:64px;display:flex;align-items:center;padding-left:20px}
.title-slide .photo{position:absolute;left:0;top:64px;width:468px;height:176px;background:linear-gradient(120deg,#b9c3c5,#d3d9da 55%,#c4cccd)}
.title-slide .claim{position:absolute;left:22px;top:136px;font:300 21px 'Raleway',sans-serif;color:#fff;letter-spacing:.5px}
.title-slide .date{position:absolute;left:22px;top:196px;font:400 5.5px 'Open Sans',sans-serif;color:#fff}
.brand{font:400 12px 'Raleway',sans-serif;color:var(--dim);line-height:1.05}
.brand.white{color:#fff}
.brand.lg{font-size:15px}

.slide{position:absolute;width:385px;height:215px;overflow:hidden;background:var(--paper)}
.abs{position:absolute}
.h{position:absolute;left:24px;top:12px;font:500 13.5px 'Roboto',sans-serif;color:var(--dim);white-space:nowrap}
.h::before{content:"";position:absolute;left:-6px;top:2px;width:1px;height:22px;background:var(--pink)}
.sub{position:absolute;left:24px;top:28px;font:400 5.5px 'Open Sans',sans-serif;color:var(--sand)}
.tx{font:400 3.8px/1.5 'Open Sans',sans-serif;color:var(--body)}
.tx.j{text-align:justify}
.lbl{font:600 5px 'Open Sans',sans-serif;color:var(--dim)}
.foot{position:absolute;left:8px;bottom:3px;font:400 4.5px 'Raleway',sans-serif;color:var(--gray)}
.page{position:absolute;right:10px;bottom:3px;font:400 3.5px 'Open Sans',sans-serif;color:var(--sand);letter-spacing:1px}
.card{position:absolute;background:#fff;box-shadow:0 1px 5px rgba(0,0,0,.12)}
.ph{position:absolute}
.dot{position:absolute;width:11px;height:11px;border-radius:50%;font:600 3.8px/11px 'Open Sans',sans-serif;color:#fff;text-align:center}
.ring{position:absolute;width:15px;height:15px;border-radius:50%;border:1.5px solid var(--sand);background:var(--soft)}
.pic{position:absolute;background:var(--sand);color:#fff;font:600 4.5px 'Open Sans',sans-serif;display:flex;align-items:center;justify-content:center}
.big{position:absolute;font:700 22px 'Roboto',sans-serif;color:#fff;text-align:center}
</style>
</head>
<body>

<!-- HERO -->
<div class="hero-bg" role="img" aria-label="Photo of a group of friends raising their hands against a hazy evening sky"></div>
<svg class="hero-light" width="1200" height="545" viewBox="0 0 1200 545"><polygon points="830,0 1200,0 1200,200" fill="#e9ebec" opacity=".85"/></svg>
<div class="title-slide">
  <div class="band"><span class="brand lg">brennig-tautz</span></div>
  <div class="photo" role="img" aria-label="Photo of hands working with charts and a laptop on a desk"></div>
  <div class="claim">COACH.&nbsp; TRAINERIN.&nbsp; BERATERIN.</div>
  <div class="date">MONTH, YEAR</div>
</div>
<div class="hero-rule"></div>

<!-- ROW 1 -->
<div class="slide" style="left:13px;top:547px;background:var(--sand)">
  <svg class="abs" width="385" height="215" viewBox="0 0 385 215" role="img" aria-label="Photo of a team working with laptops and notebooks on a wooden table"><defs><linearGradient id="g1" x1="0" x2="1" y1="0" y2="1"><stop offset="0" stop-color="#5b4a3e"/><stop offset=".6" stop-color="#8c7a69"/><stop offset="1" stop-color="#4f5e6a"/></linearGradient></defs><path d="M268 0H385V215H212C222 140 238 60 268 0Z" fill="url(#g1)"/></svg>
  <div class="abs brand white" style="left:28px;top:64px;font-size:13px">brennig-tautz</div>
  <div class="abs" style="left:28px;top:100px;font:300 13px 'Raleway',sans-serif;color:#fff">YOUR TITLE GOES HERE</div>
  <div class="abs" style="left:28px;top:116px;font:700 13px 'Raleway',sans-serif;color:#fff;letter-spacing:.5px">ONE-TWO SENTENCES</div>
  <div class="abs" style="left:28px;top:168px;width:78px;height:14px;border-radius:7px;background:var(--gray);font:600 4.2px/14px 'Open Sans',sans-serif;color:#fff;text-align:center">PRESENTER NAME</div>
</div>

<div class="slide" style="left:408px;top:547px;background:var(--teal)">
  <svg class="abs" width="385" height="215" viewBox="0 0 385 215" role="img" aria-label="Photo of a lightbox sign reading think outside the box on a dark chair"><defs><linearGradient id="g2" x1="0" x2="1"><stop offset="0" stop-color="#2c4046"/><stop offset=".55" stop-color="#53676c"/><stop offset="1" stop-color="#c9d2d4"/></linearGradient></defs><path d="M0 0H300C250 60 250 160 300 215H0Z" fill="url(#g2)"/></svg>
  <div class="abs" style="left:303px;top:20px;font:700 8.5px/1.25 'Roboto',sans-serif;color:#fff;letter-spacing:1px">COACH.<br>TRAINERIN.<br>BERATERIN.</div>
  <div class="abs brand white" style="left:300px;top:182px;font-size:11px">brennig-tautz</div>
  <div class="abs" style="left:10px;top:202px;font:400 4px 'Open Sans',sans-serif;color:#fff">MONTH, YEAR</div>
</div>

<div class="slide" style="left:804px;top:547px">
  <div class="ph" style="inset:0;background:linear-gradient(160deg,#2e3a2c,#55624b 50%,#8a7f66)" role="img" aria-label="Photo of a woman walking on a wooden bridge in a forest"></div>
  <div class="abs" style="left:92px;top:156px;width:24px;height:24px;border-radius:50%;background:rgba(156,211,209,.8);border:1.5px solid #fff"></div>
  <div class="abs" style="left:125px;top:156px;font:300 13px 'Raleway',sans-serif;color:#fff">SECTION DIVIDER</div>
  <div class="abs" style="left:125px;top:172px;font:700 5.5px 'Open Sans',sans-serif;color:#fff">SECTION SUBTITLE</div>
</div>

<!-- ROW 2 -->
<div class="slide" style="left:13px;top:770px">
  <div class="abs" style="left:0;top:0;width:88px;height:150px;background:var(--sand)"></div>
  <div class="ph" style="left:48px;top:40px;width:80px;height:124px;background:linear-gradient(#7b7b7b,#c9c9c9);border:4px solid #fff;box-shadow:0 1px 4px rgba(0,0,0,.2)" role="img" aria-label="Black and white portrait of the coach"></div>
  <div class="abs" style="left:148px;top:45px;font:500 14px 'Roboto',sans-serif;color:var(--dim)">ÜBER MICH</div>
  <div class="abs tx j" style="left:148px;top:66px;width:215px;font-size:4.1px;color:#555">Mit Feingefühl, einer wertschätzenden Haltung, Visionskraft und ausgeprägten Kommunikationsfähigkeiten begleite ich seit 22 Berufsjahren Menschen und Organisationen in unterschiedlichen Experten-, Coach-, Berater- oder Führungsrollen.<br><br>Führungskultur entwickeln, Kommunikation für Veränderung gestalten, agiles Arbeiten fördern oder die Digitalisierung vorantreiben – meine Themenfelder seit vielen Jahren, die ich immer mit dem Anspruch verfolge, Menschen einzubinden und gut mitzunehmen. Dann ich weiß, was derartige Change Prozesse für Unternehmen bedeuten.<br><br>Meine große Leidenschaft ist es deshalb, Menschen und Organisationen im Wandel zu begleiten, mit ihnen neue Möglichkeitsräume zu entdecken und sie dabei zu unterstützen, in ihre volle Kraft zu kommen.</div>
  <div class="foot">brennig-tautz</div><div class="page">PAGE · 04</div>
</div>

<div class="slide" style="left:408px;top:770px">
  <div class="h">Add Your Awesome Text Here</div><div class="sub">Write here a great subtitle</div>
  <div class="abs tx j" style="left:28px;top:60px;width:100px">There are many variations of passages of Lorem Ipsum available, but the majority have suffered alteration in some form, by injected humour, or randomised words which don't look even slightly believable. If you are going to use a passage of Lorem Ipsum, you need to be sure there isn't anything embarrassing hidden in the middle of text. All the Lorem Ipsum generators on the Internet tend to repeat predefined chunks as necessary, making this the first true generator on the Internet. It uses a dictionary of over 200 Latin words, combined with a handful of model sentence structures, to generate Lorem Ipsum which looks reasonable.</div>
  <div class="abs tx j" style="left:142px;top:60px;width:100px">Ipsum is therefore always free from repetition, injected humour, or non-characteristic words etc. There are many variations of passages of Lorem Ipsum available, but the majority have suffered alteration in some form, by injected humour, or randomised words which don't look even slightly believable. If you are going to use a passage of Lorem Ipsum, you need to be sure there isn't anything embarrassing hidden in the middle of text. All the Lorem Ipsum generators on the Internet tend to repeat predefined chunks as necessary, making this the first true generator on the Internet.</div>
  <div class="abs tx j" style="left:256px;top:60px;width:100px">passages of Lorem Ipsum available, but the majority have suffered alteration in some form, by injected humour, or randomised words which don't look even slightly believable. If you are going to use a passage of Lorem Ipsum. All the Lorem Ipsum generators on the Internet tend to repeat predefined chunks as necessary making this the first true generator on the Internet. There are many variations of passages of Lorem Ipsum available, but the majority have suffered alteration in some form, by injected humour, or randomised words which don't look even slightly believable.</div>
  <div class="foot">brennig-tautz</div><div class="page">PAGE · 05</div>
</div>

<div class="slide" style="left:804px;top:770px">
  <div class="ph" style="left:0;top:0;width:192px;height:200px;background:linear-gradient(160deg,#dfe3e4,#a9b2b4)" role="img" aria-label="Photo of a glass office tower seen from below"></div>
  <div class="abs" style="left:40px;top:62px;width:112px;font:italic 700 6.6px/1.25 'Open Sans',sans-serif;color:#fff;text-align:center">Lorem ipsum dolor sit amet, consectetur adipiscing elit, sed do eiusmod tempor incididunt ut labore et dolore magna aliqua. Lorem ipsum dolor sit amet, consectetur adipiscing elit, sed do eiusmod tempor incididunt ut labore et dolore magna aliqua.</div>
  <div class="abs" style="left:218px;top:46px;width:150px;font:400 4.6px/1.3 'Open Sans',sans-serif;color:var(--teal)">Lorem ipsum dolor sit amet, consectetur adipiscing elit, sed do eiusmod tempor incididunt ut labore et dolore magna aliqua. Lorem ipsum dolor sit amet, consectetur adipiscing elit, sed do eiusmod tempor incididunt ut labore et dolore magna aliqua.</div>
  <div class="abs" style="left:218px;top:86px;width:150px">
    <div style="display:flex;gap:8px;margin-bottom:7px"><span style="flex:none;width:6px;height:6px;border-radius:50%;border:1px solid var(--pink)"></span><span class="tx">Lorem ipsum dolor sit amet, consectetur adipiscing elit, sed do eiusmod tempor incididunt ut labore et dolore magna aliqua.</span></div>
    <div style="display:flex;gap:8px;margin-bottom:7px"><span style="flex:none;width:6px;height:6px;border-radius:50%;border:1px solid var(--pink)"></span><span class="tx">Lorem ipsum dolor sit amet, consectetur adipiscing elit, sed do eiusmod tempor incididunt ut labore et dolore magna aliqua.</span></div>
    <div style="display:flex;gap:8px;margin-bottom:7px"><span style="flex:none;width:6px;height:6px;border-radius:50%;border:1px solid var(--pink)"></span><span class="tx">Lorem ipsum dolor sit amet, consectetur adipiscing elit, sed do eiusmod tempor incididunt ut labore et dolore magna aliqua.</span></div>
    <div style="display:flex;gap:8px"><span style="flex:none;width:6px;height:6px;border-radius:50%;border:1px solid var(--pink)"></span><span class="tx">Lorem ipsum dolor sit amet, consectetur adipiscing elit, sed do eiusmod tempor incididunt ut labore et dolore magna aliqua.</span></div>
  </div>
  <div class="foot">brennig-tautz</div><div class="page">PAGE · 06</div>
</div>

<!-- ROW 3 -->
<div class="slide" style="left:13px;top:998px">
  <div class="h">Add Your Awesome Text Here</div><div class="sub">Write here a great subtitle</div>
  <div class="card" style="left:36px;top:52px;width:88px;height:130px;border-bottom:2px solid var(--pink)"><div class="abs lbl" style="left:8px;top:10px;font-size:5.5px;color:var(--gray)">Add Awesome<br>Title Here</div><div class="abs tx" style="left:8px;top:32px;width:74px">Lorem ipsum dolor sit amet, consectetur adipiscing elit, sed do eiusmod tempor incididunt ut labore et dolore magna aliqua.<br><br>• Lorem ipsum dolor sit amet, consectetur adipiscing elit, sed<br><br>• Lorem ipsum dolor sit amet, consectetur adipiscing elit, sed<br><br>• Lorem ipsum dolor sit amet, consectetur adipiscing elit, sed</div></div>
  <div class="card" style="left:144px;top:52px;width:88px;height:130px;border-bottom:2px solid var(--pink)"><div class="abs lbl" style="left:8px;top:10px;font-size:5.5px;color:var(--gray)">Add Awesome<br>Title Here</div><div class="abs tx" style="left:8px;top:32px;width:74px">Lorem ipsum dolor sit amet, consectetur adipiscing elit, sed do eiusmod tempor incididunt ut labore et dolore magna aliqua.<br><br>• Lorem ipsum dolor sit amet, consectetur adipiscing elit, sed<br><br>• Lorem ipsum dolor sit amet, consectetur adipiscing elit, sed<br><br>• Lorem ipsum dolor sit amet, consectetur adipiscing elit, sed</div></div>
  <div class="card" style="left:252px;top:52px;width:88px;height:130px;border-bottom:2px solid var(--pink)"><div class="abs lbl" style="left:8px;top:10px;font-size:5.5px;color:var(--gray)">Add Awesome<br>Title Here</div><div class="abs tx" style="left:8px;top:32px;width:74px">Lorem ipsum dolor sit amet, consectetur adipiscing elit, sed do eiusmod tempor incididunt ut labore et dolore magna aliqua.<br><br>• Lorem ipsum dolor sit amet, consectetur adipiscing elit, sed<br><br>• Lorem ipsum dolor sit amet, consectetur adipiscing elit, sed<br><br>• Lorem ipsum dolor sit amet, consectetur adipiscing elit, sed</div></div>
  <div class="foot">brennig-tautz</div><div class="page">PAGE · 07</div>
</div>

<div class="slide" style="left:408px;top:998px">
  <div class="h">Add Your Awesome Text Here</div><div class="sub">Write here a great subtitle</div>
  <div class="ring" style="left:36px;top:66px"></div><div class="abs lbl" style="left:64px;top:64px">Project name</div><div class="abs tx" style="left:64px;top:72px;width:92px">Lorem ipsum dolor sit amet, nec an dictas equidem appellantur, ut has commune accommodare. Mea illum, ludus solet idpro.</div>
  <div class="ring" style="left:36px;top:107px"></div><div class="abs lbl" style="left:64px;top:105px">Project name</div><div class="abs tx" style="left:64px;top:113px;width:92px">Lorem ipsum dolor sit amet, nec an dictas equidem appellantur, ut has commune accommodare. Mea illum, ludus solet idpro.</div>
  <div class="ring" style="left:36px;top:148px"></div><div class="abs lbl" style="left:64px;top:146px">Project name</div><div class="abs tx" style="left:64px;top:154px;width:92px">Lorem ipsum dolor sit amet, nec an dictas equidem appellantur, ut has commune accommodare. Mea illum, ludus solet idpro.</div>
  <div class="ring" style="left:202px;top:66px"></div><div class="abs lbl" style="left:230px;top:64px">Project name</div><div class="abs tx" style="left:230px;top:72px;width:92px">Lorem ipsum dolor sit amet, nec an dictas equidem appellantur, ut has commune accommodare. Mea illum, ludus solet idpro.</div>
  <div class="ring" style="left:202px;top:107px"></div><div class="abs lbl" style="left:230px;top:105px">Project name</div><div class="abs tx" style="left:230px;top:113px;width:92px">Lorem ipsum dolor sit amet, nec an dictas equidem appellantur, ut has commune accommodare. Mea illum, ludus solet idpro.</div>
  <div class="ring" style="left:202px;top:148px"></div><div class="abs lbl" style="left:230px;top:146px">Project name</div><div class="abs tx" style="left:230px;top:154px;width:92px">Lorem ipsum dolor sit amet, nec an dictas equidem appellantur, ut has commune accommodare. Mea illum, ludus solet idpro.</div>
  <div class="foot">brennig-tautz</div><div class="page">PAGE · 08</div>
</div>

<div class="slide" style="left:804px;top:998px">
  <div class="h">Add Your Awesome Text Here</div><div class="sub">Write here a great subtitle</div>
  <div class="dot" style="left:24px;top:68px;background:var(--teal)">01</div><div class="abs lbl" style="left:45px;top:67px;font-size:4.5px">Your Text Here</div><div class="abs tx" style="left:45px;top:75px">Lorem ipsum dolor sit amet.</div>
  <div class="dot" style="left:24px;top:96px;background:var(--teal)">04</div><div class="abs lbl" style="left:45px;top:95px;font-size:4.5px">Your Text Here</div><div class="abs tx" style="left:45px;top:103px">Lorem ipsum dolor sit amet.</div>
  <div class="dot" style="left:24px;top:124px;background:var(--teal)">07</div><div class="abs lbl" style="left:45px;top:123px;font-size:4.5px">Your Text Here</div><div class="abs tx" style="left:45px;top:131px">Lorem ipsum dolor sit amet.</div>
  <div class="dot" style="left:24px;top:152px;background:var(--teal)">10</div><div class="abs lbl" style="left:45px;top:151px;font-size:4.5px">Your Text Here</div><div class="abs tx" style="left:45px;top:159px">Lorem ipsum dolor sit amet.</div>
  <div class="dot" style="left:135px;top:68px;background:var(--pink)">02</div><div class="abs lbl" style="left:156px;top:67px;font-size:4.5px">Your Text Here</div><div class="abs tx" style="left:156px;top:75px">Lorem ipsum dolor sit amet.</div>
  <div class="dot" style="left:135px;top:96px;background:var(--pink)">05</div><div class="abs lbl" style="left:156px;top:95px;font-size:4.5px">Your Text Here</div><div class="abs tx" style="left:156px;top:103px">Lorem ipsum dolor sit amet.</div>
  <div class="dot" style="left:135px;top:124px;background:var(--pink)">08</div><div class="abs lbl" style="left:156px;top:123px;font-size:4.5px">Your Text Here</div><div class="abs tx" style="left:156px;top:131px">Lorem ipsum dolor sit amet.</div>
  <div class="dot" style="left:135px;top:152px;background:var(--pink)">11</div><div class="abs lbl" style="left:156px;top:151px;font-size:4.5px">Your Text Here</div><div class="abs tx" style="left:156px;top:159px">Lorem ipsum dolor sit amet.</div>
  <div class="dot" style="left:250px;top:68px;background:var(--teal)">03</div><div class="abs lbl" style="left:270px;top:67px;font-size:4.5px">Your Text Here</div><div class="abs tx" style="left:270px;top:75px">Lorem ipsum dolor sit amet.</div>
  <div class="dot" style="left:250px;top:96px;background:var(--pink)">06</div><div class="abs lbl" style="left:270px;top:95px;font-size:4.5px">Your Text Here</div><div class="abs tx" style="left:270px;top:103px">Lorem ipsum dolor sit amet.</div>
  <div class="dot" style="left:250px;top:124px;background:var(--pink)">09</div><div class="abs lbl" style="left:270px;top:123px;font-size:4.5px">Your Text Here</div><div class="abs tx" style="left:270px;top:131px">Lorem ipsum dolor sit amet.</div>
  <div class="dot" style="left:250px;top:152px;background:var(--pink)">12</div><div class="abs lbl" style="left:270px;top:151px;font-size:4.5px">Your Text Here</div><div class="abs tx" style="left:270px;top:159px">Lorem ipsum dolor sit amet.</div>
  <div class="foot">brennig-tautz</div><div class="page">PAGE · 09</div>
</div>

<!-- ROW 4 -->
<div class="slide" style="left:13px;top:1225px">
  <div class="abs" style="left:0;top:0;width:385px;height:120px;background:var(--sand)"></div>
  <div class="abs" style="left:24px;top:30px;font:700 12px/1.2 'Roboto',sans-serif;color:#fff">Your awesome<br>text here</div>
  <div class="abs" style="left:24px;top:68px;font:400 4.2px 'Open Sans',sans-serif;color:#fff;letter-spacing:2px">SUB TITLE GOES HERE</div>
  <div class="abs" style="left:185px;top:30px;width:180px;font:400 4.3px/1.45 'Open Sans',sans-serif;color:#fff">Lorem ipsum dolor sit amet, consectetur adipiscing elit, sed do eiusmod tempor incididunt ut labore et dolore magna aliqua. Lorem ipsum dolor sit amet, consectetur adipiscing elit, sed do eiusmod tempor incididunt ut labore et dolore magna aliqua. Ut enim ad minim veniam, quis nostrud exercitation ullamco laboris nisi ut aliquip.</div>
  <div class="ph" style="left:22px;top:86px;width:96px;height:62px;border-radius:4px;background:linear-gradient(#c7d4dc,#9a8b6a)" role="img" aria-label="Photo of a hand holding a compass above a landscape"></div>
  <div class="ph" style="left:145px;top:86px;width:96px;height:62px;border-radius:4px;background:linear-gradient(135deg,#b99b7c,#5d6c86)" role="img" aria-label="Photo of hands using a tablet"></div>
  <div class="ph" style="left:272px;top:86px;width:96px;height:62px;border-radius:4px;background:linear-gradient(#e6e2dc,#a3968a)" role="img" aria-label="Photo of a bright office with desks"></div>
  <div class="abs lbl" style="left:22px;top:156px;font-size:4.5px">Your Text Here</div><div class="abs tx" style="left:22px;top:164px;width:100px">Lorem ipsum dolor sit amet, consectetur adipiscing elit, sed do eiusmod tempor incididunt ut labore et dolore magna aliqua.</div>
  <div class="abs lbl" style="left:145px;top:156px;font-size:4.5px">Your Text Here</div><div class="abs tx" style="left:145px;top:164px;width:100px">Lorem ipsum dolor sit amet, consectetur adipiscing elit, sed do eiusmod tempor incididunt ut labore et dolore magna aliqua.</div>
  <div class="abs lbl" style="left:272px;top:156px;font-size:4.5px">Your Text Here</div><div class="abs tx" style="left:272px;top:164px;width:100px">Lorem ipsum dolor sit amet, consectetur adipiscing elit, sed do eiusmod tempor incididunt ut labore et dolore magna aliqua.</div>
  <div class="foot">brennig-tautz</div><div class="page">PAGE · 10</div>
</div>

<div class="slide" style="left:408px;top:1225px">
  <div class="abs" style="left:26px;top:22px;width:340px;height:168px;background:var(--soft);border-radius:4px"></div>
  <div class="abs" style="left:26px;top:40px;font:700 11px/1.1 'Roboto',sans-serif;color:var(--dim)">Add your awesome<br>text here</div>
  <div class="abs tx j" style="left:34px;top:88px;width:165px">There are many variations of passages of Lorem Ipsum available, but the majority have suffered alteration in some form, by injected humour, or randomised words which don't look even slightly believable. If you are going to use a passage of Lorem Ipsum, you need to be sure there isn't anything embarrassing hidden in the middle of text. All the Lorem Ipsum generators on the Internet tend to repeat predefined chunks as necessary, making this the first true generator on the Internet. There are many variations of passages of Lorem Ipsum available, but the majority have suffered alteration in some form, by injected humour, or randomised words which don't look even slightly believable. If you are going to use a passage of Lorem Ipsum. All the Lorem Ipsum generators on the Internet tend to repeat predefined chunks as necessary, making this the first true generator on the Internet.</div>
  <div class="ph" style="left:194px;top:22px;width:172px;height:100px;border-radius:6px;background:linear-gradient(135deg,#3f5055,#1f2a2e 60%,#5c6b70)" role="img" aria-label="Photo of a lightbox sign reading think outside the box"></div>
  <div class="abs" style="left:206px;top:106px;width:55px;height:55px;border-radius:50%;background:var(--teal);border:2px solid #fff"></div>
  <div class="abs" style="left:206px;top:118px;width:55px;text-align:center;font:500 14px 'Roboto',sans-serif;color:#fff">50%</div>
  <div class="abs" style="left:213px;top:137px;width:41px;text-align:center;font:400 3.5px/1.3 'Open Sans',sans-serif;color:#fff">Lorem ipsum dolor sit amet, consectetur adipiscing elit</div>
  <div class="foot">brennig-tautz</div><div class="page">PAGE · 11</div>
</div>

<div class="slide" style="left:804px;top:1225px">
  <div class="h">Add Your Awesome Text Here</div><div class="sub">Write here a great subtitle</div>
  <div class="pic" style="left:14px;top:44px;width:68px;height:106px">YOUR PICTURE</div>
  <div class="pic" style="left:88px;top:44px;width:166px;height:46px">YOUR PICTURE</div>
  <div class="pic" style="left:266px;top:44px;width:108px;height:84px">YOUR PICTURE</div>
  <div class="pic" style="left:88px;top:96px;width:76px;height:54px">YOUR PICTURE</div>
  <div class="pic" style="left:170px;top:96px;width:84px;height:94px">YOUR PICTURE</div>
  <div class="pic" style="left:14px;top:156px;width:150px;height:34px">YOUR PICTURE</div>
  <div class="pic" style="left:266px;top:134px;width:108px;height:56px">YOUR PICTURE</div>
  <div class="foot">brennig-tautz</div><div class="page">PAGE · 12</div>
</div>

<!-- ROW 5 -->
<div class="slide" style="left:13px;top:1453px">
  <div class="ph" style="left:58px;top:0;width:327px;height:200px;background:linear-gradient(170deg,#3e3b37,#7a6b5b 55%,#c89a64)" role="img" aria-label="Photo of a crowded city street between classic buildings at sunset"></div>
  <div class="abs" style="left:0;top:105px;width:200px;height:95px;background:var(--teal)"></div>
  <div class="abs" style="left:22px;top:113px;font:700 13px 'Roboto',sans-serif;color:#fff">Your Text Here</div>
  <div class="abs" style="left:22px;top:133px;width:170px;font:400 4.2px/1.7 'Open Sans',sans-serif;color:#fff">Lorem Ipsum is the printing and typesetting industry. Lorem Ipsum has been the industry's standard dummy text ever since the 1500s, when an unknown printer took a galley of type and scrambled it to make a type specimen book. It has survived not only five centuries.</div>
  <div class="foot">brennig-tautz</div><div class="page">PAGE · 13</div>
</div>

<div class="slide" style="left:408px;top:1453px">
  <div class="abs" style="left:24px;top:26px;font:700 12px/1.2 'Roboto',sans-serif;color:var(--dim)">Add your Awesome<br>Text Here</div>
  <div class="abs tx" style="left:24px;top:62px;width:160px;color:#666">Lorem Ipsum is the printing and typesetting industry. Lorem Ipsum has been the industry's standard dummy text ever since the 1500s, when an unknown printer took a galley of type and scrambled it to make a type specimen book. It has survived not only five centuries.</div>
  <div class="ph" style="left:228px;top:14px;width:145px;height:188px;border-radius:8px;background:linear-gradient(135deg,#f3eadf,#f0c48e 50%,#3c3c3c)" role="img" aria-label="Photo of a hand placing sticky notes on a wall"></div>
  <div class="card" style="left:24px;top:110px;width:75px;height:74px;background:var(--teal);border-radius:3px"><div class="abs lbl" style="left:0;right:0;top:28px;text-align:center;color:#fff;font-size:4.2px">Project name</div><div class="abs tx" style="left:6px;right:6px;top:36px;text-align:center;color:#fff">Lorem ipsum dolor sit amet, nec an dictas equidem appellantur, ut has commune accommodare. Mea illum, ludus solet idpro.</div></div>
  <div class="card" style="left:106px;top:110px;width:75px;height:74px;border-radius:3px"><div class="abs lbl" style="left:0;right:0;top:28px;text-align:center;font-size:4.2px">Project name</div><div class="abs tx" style="left:6px;right:6px;top:36px;text-align:center">Lorem ipsum dolor sit amet, nec an dictas equidem appellantur, ut has commune accommodare. Mea illum, ludus solet idpro.</div></div>
  <div class="card" style="left:188px;top:110px;width:75px;height:74px;border-radius:3px"><div class="abs lbl" style="left:0;right:0;top:28px;text-align:center;font-size:4.2px">Project name</div><div class="abs tx" style="left:6px;right:6px;top:36px;text-align:center">Lorem ipsum dolor sit amet, nec an dictas equidem appellantur, ut has commune accommodare. Mea illum, ludus solet idpro.</div></div>
  <div class="foot">brennig-tautz</div><div class="page">PAGE · 14</div>
</div>

<div class="slide" style="left:804px;top:1453px">
  <div class="abs" style="left:18px;top:48px;font:700 11px/1.25 'Roboto',sans-serif;color:var(--dim)">Lorem ipsum dolor sit<br>amet elit et dolor</div>
  <div class="abs tx" style="left:18px;top:80px;width:150px">Lorem ipsum dolor sit amet, consectetur adipiscing elit, sed do eiusmod tempor incididunt ut labore et dolore magna aliqua. Lorem ipsum dolor sit amet, consectetur adipiscing elit, sed do eiusmod.</div>
  <div class="ph" style="left:176px;top:32px;width:195px;height:112px;background:linear-gradient(135deg,#d9dcdd,#6e7274)" role="img" aria-label="Black and white photo of a modern lounge with chairs"></div>
  <div class="abs" style="left:0;top:142px;width:128px;height:58px;background:var(--teal)"></div>
  <div class="abs" style="left:128px;top:142px;width:128px;height:58px;background:var(--pink)"></div>
  <div class="abs" style="left:256px;top:142px;width:129px;height:58px;background:var(--sand)"></div>
  <div class="abs" style="left:24px;top:128px;width:28px;height:28px;border-radius:50%;background:var(--teal);border:2px solid #fff"></div>
  <div class="abs" style="left:152px;top:128px;width:28px;height:28px;border-radius:50%;background:var(--pink);border:2px solid #fff"></div>
  <div class="abs" style="left:280px;top:128px;width:28px;height:28px;border-radius:50%;background:var(--sand);border:2px solid #fff"></div>
  <div class="abs lbl" style="left:12px;top:163px;color:#fff;font-size:4.5px">Lorem ipsum dolor</div><div class="abs tx" style="left:12px;top:171px;width:108px;color:#fff">Lorem ipsum dolor sit amet, consectetur adipiscing elit, sed do eiusmod tempor incididunt ut labore et dolore magna aliqua.</div>
  <div class="abs lbl" style="left:140px;top:163px;color:#fff;font-size:4.5px">Lorem ipsum dolor</div><div class="abs tx" style="left:140px;top:171px;width:108px;color:#fff">Lorem ipsum dolor sit amet, consectetur adipiscing elit, sed do eiusmod tempor incididunt ut labore et dolore magna aliqua.</div>
  <div class="abs lbl" style="left:268px;top:163px;color:#fff;font-size:4.5px">Lorem ipsum dolor</div><div class="abs tx" style="left:268px;top:171px;width:108px;color:#fff">Lorem ipsum dolor sit amet, consectetur adipiscing elit, sed do eiusmod tempor incididunt ut labore et dolore magna aliqua.</div>
  <div class="foot">brennig-tautz</div><div class="page">PAGE · 15</div>
</div>

<!-- ROW 6 -->
<div class="slide" style="left:13px;top:1680px">
  <div class="h">Add Your Awesome Text Here</div><div class="sub">Write here a great subtitle</div>
  <svg class="abs" style="left:0;top:0" width="385" height="215" viewBox="0 0 385 215">
    <g transform="rotate(-90 192 122)" fill="none" stroke-width="20">
      <circle cx="192" cy="122" r="44" stroke="#9cd3d1" stroke-dasharray="42 234.5" stroke-dashoffset="0"/>
      <circle cx="192" cy="122" r="44" stroke="#f6ded1" stroke-dasharray="42 234.5" stroke-dashoffset="-46"/>
      <circle cx="192" cy="122" r="44" stroke="#9cd3d1" stroke-dasharray="42 234.5" stroke-dashoffset="-92"/>
      <circle cx="192" cy="122" r="44" stroke="#f6ded1" stroke-dasharray="42 234.5" stroke-dashoffset="-138"/>
      <circle cx="192" cy="122" r="44" stroke="#bfcbce" stroke-dasharray="42 234.5" stroke-dashoffset="-184"/>
      <circle cx="192" cy="122" r="44" stroke="#f6ded1" stroke-dasharray="42 234.5" stroke-dashoffset="-230"/>
    </g>
  </svg>
  <div class="abs brand" style="left:162px;top:116px;width:60px;text-align:center;font-size:8.5px">brennig-tautz</div>
  <div class="abs lbl" style="left:86px;top:52px">Lorem ipsum dolor</div><div class="abs tx" style="left:46px;top:60px;width:95px;text-align:center">Lorem ipsum dolor sit amet, consectetur adipiscing elit, sed do eiusmod tempor</div>
  <div class="abs lbl" style="left:60px;top:106px">Lorem ipsum dolor</div><div class="abs tx" style="left:28px;top:114px;width:95px;text-align:center">Lorem ipsum dolor sit amet, consectetur adipiscing elit, sed do eiusmod tempor</div>
  <div class="abs lbl" style="left:86px;top:160px">Lorem ipsum dolor</div><div class="abs tx" style="left:50px;top:168px;width:95px;text-align:center">Lorem ipsum dolor sit amet, consectetur adipiscing elit, sed do eiusmod tempor</div>
  <div class="abs lbl" style="left:248px;top:52px">Lorem ipsum dolor</div><div class="abs tx" style="left:248px;top:60px;width:95px">Lorem ipsum dolor sit amet, consectetur adipiscing elit, sed do eiusmod tempor</div>
  <div class="abs lbl" style="left:268px;top:106px">Lorem ipsum dolor</div><div class="abs tx" style="left:268px;top:114px;width:95px">Lorem ipsum dolor sit amet, consectetur adipiscing elit, sed do eiusmod tempor</div>
  <div class="abs lbl" style="left:250px;top:160px">Lorem ipsum dolor</div><div class="abs tx" style="left:250px;top:168px;width:95px">Lorem ipsum dolor sit amet, consectetur adipiscing elit, sed do eiusmod tempor</div>
  <div class="foot">brennig-tautz</div><div class="page">PAGE · 16</div>
</div>

<div class="slide" style="left:408px;top:1680px">
  <div class="h">Add Your Awesome Text Here</div><div class="sub">Write here a great subtitle</div>
  <div class="abs" style="left:52px;top:121px;width:280px;height:1px;background:var(--sand)"></div>
  <div class="abs" style="left:40px;top:108px;width:26px;height:26px;border-radius:50%;background:var(--teal);border:3px solid #e4f4f3"></div>
  <div class="abs" style="left:109px;top:108px;width:26px;height:26px;border-radius:50%;background:var(--pink);border:3px solid #fbefe8"></div>
  <div class="abs" style="left:178px;top:108px;width:26px;height:26px;border-radius:50%;background:var(--teal);border:3px solid #e4f4f3"></div>
  <div class="abs" style="left:247px;top:108px;width:26px;height:26px;border-radius:50%;background:var(--pink);border:3px solid #fbefe8"></div>
  <div class="abs" style="left:316px;top:108px;width:26px;height:26px;border-radius:50%;background:var(--teal);border:3px solid #e4f4f3"></div>
  <div class="abs lbl" style="left:14px;top:58px;width:80px;text-align:center;font-size:4.2px">Content Title here</div><div class="abs tx" style="left:14px;top:66px;width:80px;text-align:center">Lorem ipsum dolor sit amet, nec an dictas equidem appellantur, ut has commune</div>
  <div class="abs lbl" style="left:152px;top:58px;width:80px;text-align:center;font-size:4.2px">Content Title here</div><div class="abs tx" style="left:152px;top:66px;width:80px;text-align:center">Lorem ipsum dolor sit amet, nec an dictas equidem appellantur, ut has commune</div>
  <div class="abs lbl" style="left:290px;top:58px;width:80px;text-align:center;font-size:4.2px">Content Title here</div><div class="abs tx" style="left:290px;top:66px;width:80px;text-align:center">Lorem ipsum dolor sit amet, nec an dictas equidem appellantur, ut has commune</div>
  <div class="abs lbl" style="left:82px;top:158px;width:80px;text-align:center;font-size:4.2px">Content Title here</div><div class="abs tx" style="left:82px;top:166px;width:80px;text-align:center">Promotion an ourselves up otherwise my. High what each snug rich far inhabiting</div>
  <div class="abs lbl" style="left:220px;top:158px;width:80px;text-align:center;font-size:4.2px">Content Title here</div><div class="abs tx" style="left:220px;top:166px;width:80px;text-align:center">Promotion an ourselves up otherwise my. High what each snug rich far inhabiting</div>
  <div class="foot">brennig-tautz</div><div class="page">PAGE · 17</div>
</div>

<div class="slide" style="left:804px;top:1680px">
  <div class="h">Add Your Awesome Text Here</div><div class="sub">Write here a great subtitle</div>
  <div class="abs" style="left:34px;top:60px;width:312px;height:20px;background:var(--sand)"></div>
  <div class="abs" style="left:192px;top:60px;width:78px;height:20px;background:#fff;border:1px solid var(--sand)"></div>
  <div class="abs" style="left:192px;top:80px;width:78px;height:90px;background:var(--teal)"></div>
  <div class="abs" style="left:34px;top:80px;width:158px;height:90px;background:var(--soft)"></div>
  <div class="abs" style="left:270px;top:80px;width:76px;height:90px;background:var(--soft)"></div>
  <div class="abs" style="left:34px;top:125px;width:312px;height:1px;background:#fff"></div>
  <div class="abs" style="left:113px;top:60px;width:1px;height:110px;background:#fff"></div>
  <div class="abs lbl" style="left:42px;top:68px;color:#fff;font-size:4px">ADD YOUR TITLE</div>
  <div class="abs lbl" style="left:120px;top:68px;color:#fff;font-size:4px">ADD YOUR TITLE</div>
  <div class="abs brand" style="left:202px;top:66px;font-size:6.5px">brennig-tautz</div>
  <div class="abs lbl" style="left:278px;top:68px;color:#fff;font-size:4px">ADD YOUR TITLE</div>
  <div class="abs lbl" style="left:42px;top:88px;font-size:4px">Project name</div><div class="abs tx" style="left:42px;top:95px;width:64px">Lorem Ipsum is simply dummy unknown printer took a galley of type and scrambled it to make.</div>
  <div class="abs lbl" style="left:120px;top:88px;font-size:4px">Project name</div><div class="abs tx" style="left:120px;top:95px;width:64px">Lorem Ipsum is simply dummy unknown printer took a galley of type and scrambled it to make.</div>
  <div class="abs lbl" style="left:199px;top:88px;font-size:4px;color:#fff">Project name</div><div class="abs tx" style="left:199px;top:95px;width:64px;color:#fff">Lorem Ipsum is simply dummy unknown printer took a galley of type and scrambled it to make.</div>
  <div class="abs lbl" style="left:278px;top:88px;font-size:4px">Project name</div><div class="abs tx" style="left:278px;top:95px;width:64px">Lorem Ipsum is simply dummy unknown printer took a galley of type and scrambled it to make.</div>
  <div class="abs lbl" style="left:42px;top:132px;font-size:4px">Project name</div><div class="abs tx" style="left:42px;top:139px;width:64px">Lorem Ipsum is simply dummy unknown printer took a galley of type and scrambled it to make.</div>
  <div class="abs lbl" style="left:120px;top:132px;font-size:4px">Project name</div><div class="abs tx" style="left:120px;top:139px;width:64px">Lorem Ipsum is simply dummy unknown printer took a galley of type and scrambled it to make.</div>
  <div class="abs lbl" style="left:199px;top:132px;font-size:4px;color:#fff">Project name</div><div class="abs tx" style="left:199px;top:139px;width:64px;color:#fff">Lorem Ipsum is simply dummy unknown printer took a galley of type and scrambled it to make.</div>
  <div class="abs lbl" style="left:278px;top:132px;font-size:4px">Project name</div><div class="abs tx" style="left:278px;top:139px;width:64px">Lorem Ipsum is simply dummy unknown printer took a galley of type and scrambled it to make.</div>
  <div class="foot">brennig-tautz</div><div class="page">PAGE · 18</div>
</div>

<!-- ROW 7 -->
<div class="slide" style="left:13px;top:1907px">
  <div class="h">Add Your Awesome Text Here</div><div class="sub">Write here a great subtitle</div>
  <div class="abs" style="left:36px;top:58px;width:76px;height:76px;border-radius:50%;background:var(--teal);border:4px solid #e6f5f4"></div>
  <div class="abs" style="left:158px;top:58px;width:76px;height:76px;border-radius:50%;background:var(--pink);border:4px solid #fcf1eb"></div>
  <div class="abs" style="left:280px;top:58px;width:76px;height:76px;border-radius:50%;background:var(--sand);border:4px solid #eef1f2"></div>
  <div class="big" style="left:36px;top:72px;width:76px">$1M</div>
  <div class="big" style="left:158px;top:72px;width:76px">$10M</div>
  <div class="big" style="left:280px;top:72px;width:76px">$15M</div>
  <div class="abs tx" style="left:50px;top:100px;width:48px;text-align:center;color:#fff;font-size:3.4px">Lorem ipsum dolor sit amet, nec an dictas equidem appellantur, ut has</div>
  <div class="abs tx" style="left:172px;top:100px;width:48px;text-align:center;color:#fff;font-size:3.4px">Lorem ipsum dolor sit amet, nec an dictas equidem appellantur, ut has</div>
  <div class="abs tx" style="left:294px;top:100px;width:48px;text-align:center;color:#fff;font-size:3.4px">Lorem ipsum dolor sit amet, nec an dictas equidem appellantur, ut has</div>
  <div class="abs" style="left:74px;top:138px;width:1px;height:42px;border-left:1px dashed var(--sand)"></div>
  <div class="abs" style="left:196px;top:138px;width:1px;height:42px;border-left:1px dashed var(--sand)"></div>
  <div class="abs" style="left:318px;top:138px;width:1px;height:42px;border-left:1px dashed var(--sand)"></div>
  <div class="abs lbl" style="left:30px;top:146px;width:88px;text-align:center">Lorem ipsum dolor</div><div class="abs tx" style="left:30px;top:154px;width:88px;text-align:center">Lorem ipsum dolor sit amet, consectetur adipiscing elit, sed do eiusmod tempor</div>
  <div class="abs lbl" style="left:152px;top:146px;width:88px;text-align:center">Lorem ipsum dolor</div><div class="abs tx" style="left:152px;top:154px;width:88px;text-align:center">Lorem ipsum dolor sit amet, consectetur adipiscing elit, sed do eiusmod tempor</div>
  <div class="abs lbl" style="left:274px;top:146px;width:88px;text-align:center">Lorem ipsum dolor</div><div class="abs tx" style="left:274px;top:154px;width:88px;text-align:center">Lorem ipsum dolor sit amet, consectetur adipiscing elit, sed do eiusmod tempor</div>
  <div class="foot">brennig-tautz</div><div class="page">PAGE · 19</div>
</div>

<div class="slide" style="left:408px;top:1907px">
  <div class="abs" style="left:0;right:0;top:40px;text-align:center;font:500 15px 'Roboto',sans-serif;color:var(--dim)">Your awesome text here</div>
  <div class="abs tx" style="left:82px;top:62px;width:220px;text-align:center;color:#666">Lorem Ipsum the printing and typesetting industry. Lorem Ipsum has been the industry's standard dummy text ever since the 1500s, when an unknown printer took a galley of type and scrambled it to make a type specimen book. It has survived not only five centuries.</div>
  <svg class="abs" style="left:0;top:0" width="385" height="215" viewBox="0 0 385 215" fill="none" stroke-width="3.5">
    <circle cx="108" cy="129" r="24" stroke="#eeeeee"/><circle cx="108" cy="129" r="24" stroke="#f6ded1" stroke-dasharray="75.4 150.8" transform="rotate(-90 108 129)"/>
    <circle cx="190" cy="129" r="24" stroke="#eeeeee"/><circle cx="190" cy="129" r="24" stroke="#9cd3d1" stroke-dasharray="113.1 150.8" transform="rotate(-90 190 129)"/>
    <circle cx="272" cy="129" r="24" stroke="#eeeeee"/><circle cx="272" cy="129" r="24" stroke="#bfcbce" stroke-dasharray="60.3 150.8" transform="rotate(-90 272 129)"/>
  </svg>
  <div class="abs" style="left:84px;top:123px;width:48px;text-align:center;font:500 10px 'Roboto',sans-serif;color:var(--dim)">50%</div>
  <div class="abs" style="left:166px;top:123px;width:48px;text-align:center;font:500 10px 'Roboto',sans-serif;color:var(--dim)">75%</div>
  <div class="abs" style="left:248px;top:123px;width:48px;text-align:center;font:500 10px 'Roboto',sans-serif;color:var(--dim)">40%</div>
  <div class="abs tx" style="left:82px;top:163px;width:52px;text-align:center">Lorem ipsum dolor amet consectetur dolor</div>
  <div class="abs tx" style="left:164px;top:163px;width:52px;text-align:center">Lorem ipsum dolor amet consectetur dolor</div>
  <div class="abs tx" style="left:246px;top:163px;width:52px;text-align:center">Lorem ipsum dolor amet consectetur dolor</div>
  <div class="foot">brennig-tautz</div><div class="page">PAGE · 20</div>
</div>

<div class="slide" style="left:804px;top:1907px">
  <svg class="abs" style="left:0;top:0" width="385" height="215" viewBox="0 0 385 215">
    <g stroke="#ececec" stroke-width=".5">
      <line x1="40" x2="200" y1="25" y2="25"/><line x1="40" x2="200" y1="40" y2="40"/><line x1="40" x2="200" y1="55" y2="55"/><line x1="40" x2="200" y1="70" y2="70"/><line x1="40" x2="200" y1="85" y2="85"/><line x1="40" x2="200" y1="100" y2="100"/><line x1="40" x2="200" y1="115" y2="115"/><line x1="40" x2="200" y1="130" y2="130"/><line x1="40" x2="200" y1="145" y2="145"/><line x1="40" x2="200" y1="160" y2="160"/>
    </g>
    <line x1="40" x2="200" y1="175" y2="175" stroke="#cccccc" stroke-width=".6"/>
    <g font-family="Open Sans,sans-serif" font-size="3.5" fill="#888" text-anchor="end">
      <text x="34" y="27">5</text><text x="34" y="42">4.5</text><text x="34" y="57">4</text><text x="34" y="72">3.5</text><text x="34" y="87">3</text><text x="34" y="102">2.5</text><text x="34" y="117">2</text><text x="34" y="132">1.5</text><text x="34" y="147">1</text><text x="34" y="162">0.5</text><text x="34" y="177">0</text>
    </g>
    <rect x="50" y="85" width="6" height="90" fill="#bfcbce"/><rect x="57" y="103" width="6" height="72" fill="#f6ded1"/><rect x="64" y="46" width="6" height="129" fill="#9cd3d1"/>
    <rect x="90" y="115" width="6" height="60" fill="#bfcbce"/><rect x="97" y="43" width="6" height="132" fill="#f6ded1"/><rect x="104" y="100" width="6" height="75" fill="#9cd3d1"/>
    <rect x="130" y="70" width="6" height="105" fill="#bfcbce"/><rect x="137" y="121" width="6" height="54" fill="#f6ded1"/><rect x="144" y="85" width="6" height="90" fill="#9cd3d1"/>
    <rect x="170" y="40" width="6" height="135" fill="#bfcbce"/><rect x="177" y="91" width="6" height="84" fill="#f6ded1"/><rect x="184" y="115" width="6" height="60" fill="#9cd3d1"/>
    <g font-family="Open Sans,sans-serif" font-size="3.5" fill="#888" text-anchor="middle"><text x="60" y="183">Category 1</text><text x="100" y="183">Category 2</text><text x="140" y="183">Category 3</text><text x="180" y="183">Category 4</text></g>
  </svg>
  <div class="abs" style="left:242px;top:36px;font:400 4px 'Open Sans',sans-serif;color:var(--gray);letter-spacing:2px">LOREM IPSUM DOLOR</div>
  <div class="abs" style="left:242px;top:46px;font:700 15px/1.2 'Roboto',sans-serif;color:var(--gray)">Company<br>Statistics</div>
  <div class="ring" style="left:242px;top:108px;border-color:var(--teal);background:#fff"></div>
  <div class="abs lbl" style="left:266px;top:107px;font-size:4.2px">Description here</div><div class="abs tx" style="left:266px;top:115px;width:70px">Our mission is delivering creative solution through visual</div>
  <div class="ring" style="left:242px;top:144px;border-color:var(--teal);background:#fff"></div>
  <div class="abs lbl" style="left:266px;top:143px;font-size:4.2px">Description here</div><div class="abs tx" style="left:266px;top:151px;width:70px">Our mission is delivering creative solution through visual</div>
  <div class="foot">brennig-tautz</div><div class="page">PAGE · 21</div>
</div>

<!-- ROW 8 -->
<div class="slide" style="left:13px;top:2131px">
  <div class="h">Add Your Awesome Text Here</div><div class="sub">Write here a great subtitle</div>
  <svg class="abs" style="left:0;top:0" width="385" height="215" viewBox="0 0 385 215">
    <rect x="40" y="72" width="14" height="110" fill="#9cd3d1"/>
    <rect x="72" y="134" width="14" height="48" fill="#f6ded1"/>
    <rect x="104" y="106" width="14" height="76" fill="#bfcbce"/>
    <rect x="136" y="154" width="14" height="28" fill="#807f84"/>
    <line x1="30" x2="160" y1="182" y2="182" stroke="#cccccc" stroke-width=".6"/>
    <g font-family="Open Sans,sans-serif" font-size="4" font-weight="600" fill="#fff" text-anchor="middle">
      <rect x="41" y="60" width="12" height="8" fill="#d9d9d9"/><text x="47" y="66" fill="#555">80</text>
      <rect x="73" y="122" width="12" height="8" fill="#d9d9d9"/><text x="79" y="128" fill="#555">35</text>
      <rect x="105" y="94" width="12" height="8" fill="#d9d9d9"/><text x="111" y="100" fill="#555">55</text>
      <rect x="137" y="142" width="12" height="8" fill="#d9d9d9"/><text x="143" y="148" fill="#555">20</text>
    </g>
    <g font-family="Open Sans,sans-serif" font-size="3.5" fill="#888" text-anchor="middle"><text x="47" y="189">Category 1</text><text x="79" y="189">Category 2</text><text x="111" y="189">Category 3</text><text x="143" y="189">Category 4</text></g>
  </svg>
  <div class="abs" style="left:200px;top:72px;width:160px">
    <div style="display:flex;gap:7px;margin-bottom:10px"><span style="flex:none;width:6px;height:6px;border-radius:50%;border:1px solid var(--pink)"></span><span class="tx" style="color:#666">Lorem ipsum dolor sit amet, quam id eros. Vestibulum luctus velit. Pretium ante, integer a blandit. Nullam nunc wisi, rutrum rhoncus Libero commodo. Ut a.</span></div>
    <div style="display:flex;gap:7px;margin-bottom:10px"><span style="flex:none;width:6px;height:6px;border-radius:50%;border:1px solid var(--pink)"></span><span class="tx" style="color:#666">Imperdiet in pulvinar. Tellus augue. Elit urna dignissim. Est inceptos. Ligula augue, etiam sit, et vestibulum.</span></div>
    <div style="display:flex;gap:7px"><span style="flex:none;width:6px;height:6px;border-radius:50%;border:1px solid var(--pink)"></span><span class="tx" style="color:#666">Dolor lacus gravida. Elit placerat risus, cursus orci, eget blandit. Et maecenas. Lorem mollis. Vestibulum feugiat pulvinar, tortor donec massa. Enim hendrerit proin. Rutrum consectetuer quis wisi vel, wisi ante.</span></div>
  </div>
  <div class="foot">brennig-tautz</div><div class="page">PAGE · 22</div>
</div>

<div class="slide" style="left:408px;top:2131px">
  <svg class="abs" style="left:0;top:0" width="385" height="215" viewBox="0 0 385 215" fill="none">
    <g stroke="#f0f0f0" stroke-width=".5"><line x1="22" x2="212" y1="60" y2="60"/><line x1="22" x2="212" y1="90" y2="90"/><line x1="22" x2="212" y1="120" y2="120"/><line x1="22" x2="212" y1="150" y2="150"/></g>
    <line x1="22" x2="212" y1="180" y2="180" stroke="#cccccc" stroke-width=".6"/>
    <path d="M26 156 C36 150 40 104 50 110 S62 172 72 168 S88 72 98 88 S110 162 122 150 S138 128 148 140 S160 80 170 66 S184 152 194 150 S204 112 210 120" stroke="#f6ded1" stroke-width="1.6"/>
    <path d="M26 150 C36 140 42 128 52 132 S64 170 76 160 S92 116 104 134 S118 176 128 162 S142 120 152 138 S168 170 178 150 S196 96 210 110" stroke="#9cd3d1" stroke-width="1.6"/>
    <g font-family="Open Sans,sans-serif" font-size="3.6" fill="#666"><text x="44" y="106">4.4</text><text x="94" y="84">5.7</text><text x="166" y="62">6.7</text><text x="196" y="108">5.6</text><text x="30" y="147">2.4</text><text x="62" y="168">1.8</text><text x="102" y="130">3.2</text><text x="120" y="170">1.2</text><text x="76" y="152">2.8</text><text x="148" y="146">2.4</text><text x="176" y="146">2.9</text><text x="204" y="147">2.4</text></g>
    <g font-family="Open Sans,sans-serif" font-size="3.2" fill="#888" text-anchor="middle"><text x="28" y="188">2005</text><text x="44" y="188">2006</text><text x="60" y="188">2007</text><text x="76" y="188">2008</text><text x="92" y="188">2009</text><text x="108" y="188">2010</text><text x="124" y="188">2011</text><text x="140" y="188">2012</text><text x="156" y="188">2013</text><text x="172" y="188">2014</text><text x="188" y="188">2015</text><text x="204" y="188">2016</text></g>
  </svg>
  <div class="abs" style="left:240px;top:68px;font:500 15px 'Roboto',sans-serif;color:var(--dim)">Chart</div>
  <div class="abs" style="left:240px;top:88px;font:400 6px 'Open Sans',sans-serif;color:var(--dim)">Lorem ipsum dolor sit amet</div>
  <div class="abs" style="left:240px;top:108px;width:120px">
    <div style="display:flex;gap:6px;margin-bottom:8px"><span style="flex:none;color:var(--teal);font-size:5px;line-height:5px">›</span><span class="tx">Lorem ipsum dolor sit amet, consectetur adipiscing elit, sed do eiusmod tempor incididunt ut labore et dolore magna aliqua.</span></div>
    <div style="display:flex;gap:6px"><span style="flex:none;color:var(--teal);font-size:5px;line-height:5px">›</span><span class="tx">Lorem ipsum dolor sit amet, consectetur adipiscing elit. Lorem ipsum dolor sit amet, consectetur adipiscing elit, sed do eiusmod tempor incididunt ut labore et dolore magna aliqua.</span></div>
  </div>
  <div class="foot">brennig-tautz</div><div class="page">PAGE · 23</div>
</div>

<div class="slide" style="left:804px;top:2131px">
  <div class="h">Add Your Awesome Text Here</div><div class="sub">Write here a great subtitle</div>
  <svg class="abs" style="left:0;top:0" width="385" height="215" viewBox="0 0 385 215" fill="none" stroke="#bfcbce" stroke-width="1">
    <path d="M20 36 C20 60 50 64 80 64 H330 C360 64 372 90 372 110 C372 130 360 136 330 136 H60 C36 136 24 150 24 166 C24 184 40 196 60 196 H385"/>
  </svg>
  <div class="abs" style="left:76px;top:60px;width:8px;height:8px;border-radius:50%;background:var(--pink)"></div>
  <div class="abs" style="left:166px;top:60px;width:8px;height:8px;border-radius:50%;background:var(--teal)"></div>
  <div class="abs" style="left:256px;top:60px;width:8px;height:8px;border-radius:50%;background:var(--pink)"></div>
  <div class="abs" style="left:76px;top:132px;width:8px;height:8px;border-radius:50%;background:var(--teal)"></div>
  <div class="abs" style="left:166px;top:132px;width:8px;height:8px;border-radius:50%;background:var(--pink)"></div>
  <div class="abs" style="left:256px;top:132px;width:8px;height:8px;border-radius:50%;background:var(--teal)"></div>
  <div class="abs" style="left:76px;top:69px;width:50px;height:7px;border-radius:4px;background:var(--pink);font:600 4px/7px 'Open Sans',sans-serif;color:#fff;padding-left:5px">2015</div>
  <div class="abs" style="left:166px;top:69px;width:50px;height:7px;border-radius:4px;background:var(--teal);font:600 4px/7px 'Open Sans',sans-serif;color:#fff;padding-left:5px">2016</div>
  <div class="abs" style="left:256px;top:69px;width:50px;height:7px;border-radius:4px;background:var(--pink);font:600 4px/7px 'Open Sans',sans-serif;color:#fff;padding-left:5px">2017</div>
  <div class="abs" style="left:76px;top:141px;width:50px;height:7px;border-radius:4px;background:var(--teal);font:600 4px/7px 'Open Sans',sans-serif;color:#fff;padding-left:5px">2018</div>
  <div class="abs" style="left:166px;top:141px;width:50px;height:7px;border-radius:4px;background:var(--pink);font:600 4px/7px 'Open Sans',sans-serif;color:#fff;padding-left:5px">2019</div>
  <div class="abs" style="left:256px;top:141px;width:50px;height:7px;border-radius:4px;background:var(--teal);font:600 4px/7px 'Open Sans',sans-serif;color:#fff;padding-left:5px">2020</div>
  <div class="abs tx" style="left:80px;top:80px;width:55px">Lorem Ipsum is simply dummy unknown printer took a galley of type and scrambled it to make.</div>
  <div class="abs tx" style="left:170px;top:80px;width:55px">Lorem Ipsum is simply dummy unknown printer took a galley of type and scrambled it to make.</div>
  <div class="abs tx" style="left:260px;top:80px;width:55px">Lorem Ipsum is simply dummy unknown printer took a galley of type and scrambled it to make.</div>
  <div class="abs tx" style="left:80px;top:152px;width:55px">Lorem Ipsum is simply dummy unknown printer took a galley of type and scrambled it to make.</div>
  <div class="abs tx" style="left:170px;top:152px;width:55px">Lorem Ipsum is simply dummy unknown printer took a galley of type and scrambled it to make.</div>
  <div class="abs tx" style="left:260px;top:152px;width:55px">Lorem Ipsum is simply dummy unknown printer took a galley of type and scrambled it to make.</div>
  <div class="foot">brennig-tautz</div><div class="page">PAGE · 24</div>
</div>

</body>
</html>
```